Report presentation for measurement or inline reports

First page of report. Our inline reporting will come in a maintenance map. We want a modern first page and a real eye-catcher for a new company based in the Netherlands called: RTP Luchtregeling B.V. We are a service company witch measures, balances and give advices at indoor climate HVAC installations. We would like to see designs that use the color blue. We deliver our services to different buildings: Hospitals, atractions, officebuildings, government buildings, swimming pools and schools. Our website: www.rtpl.nl
Updates

Can you all add the new logo please. The companyname is RTP Luchtregeling B.V.. In witch format can i retrieve the design?

Industry/Entity Type

It Company

Colors
0255a3
3176b5
85abd2
cedeed
eaf1f7
ffffff

Requirements
Must have
• Projectname; projectplace; Inline or measure report; date; logo; companyname. it must be easy printable so not to much colours.
• The companyname is: RTP Luchtregeling B.V.. Please add the name. A new logo is updated.
Nice to have
• Maybe some pictures from hvac installations, buildings or measure

```html
<!DOCTYPE html>
<html lang="en">
<head>
<meta charset="utf-8">
<title>Inline Report – Cover</title>
<link rel="stylesheet" href="https://fonts.googleapis.com/css2?family=Arimo:wght@400;700&display=swap">
<style>
  :root {
    --stage: #2b2b2b;
    --brand-blue: #2e7bbf;
    --brand-deep: #0255a3;
    --photo-dark: #1d4f80;
    --photo-mid: #3176b5;
    --photo-light: #85abd2;
    --paper: #ffffff;
    --rule: #cedeed;
  }
  * { margin: 0; padding: 0; box-sizing: border-box; }
  html, body {
    width: 1200px;
    height: 1000px;
    overflow: hidden;
    background: var(--stage);
    font-family: "Arimo", Arial, sans-serif;
  }
  .report-cover {
    position: absolute;
    left: 278px;
    top: 10px;
    width: 690px;
    height: 975px;
    background: var(--brand-blue);
    border: 1px solid var(--rule);
    color: var(--paper);
    overflow: hidden;
  }
  .logo-tab {
    position: absolute;
    left: 217px;
    top: -1px;
    width: 241px;
    height: 144px;
  }
  .logo-tab svg { position: absolute; inset: 0; }
  .logo-lockup {
    position: absolute;
    left: 0;
    right: 0;
    top: 50px;
    display: flex;
    align-items: center;
    justify-content: center;
    gap: 10px;
  }
  .logo-mark {
    width: 26px;
    height: 26px;
    background: var(--brand-deep);
  }
  .logo-name {
    font-weight: 700;
    font-size: 20px;
    color: var(--brand-deep);
    letter-spacing: 0.3px;
  }
  .report-type {
    position: absolute;
    top: 202px;
    left: 0;
    right: 0;
    text-align: center;
    padding-left: 20px;
    font-size: 72px;
    font-weight: 400;
    letter-spacing: 0.5px;
  }
  .hero-band {
    position: absolute;
    left: 0;
    right: 0;
    top: 337px;
    height: 317px;
    border-top: 2px solid var(--rule);
    border-bottom: 2px solid var(--rule);
    background: linear-gradient(160deg, var(--photo-light) 0%, var(--photo-mid) 45%, var(--photo-dark) 100%);
  }
  .project-title {
    position: absolute;
    top: 692px;
    left: 0;
    right: 0;
    text-align: center;
    padding-left: 20px;
    font-size: 32px;
  }
  .project-meta {
    position: absolute;
    top: 737px;
    left: 0;
    right: 0;
    text-align: center;
    padding-left: 14px;
    font-size: 13.5px;
  }
</style>
</head>
<body>
  <main class="report-cover">
    <header class="logo-tab">
      <svg width="241" height="144" viewBox="0 0 241 144" aria-hidden="true">
        <polygon points="0,0 241,0 241,119 120,144 0,119" fill="var(--paper)"/>
      </svg>
      <div class="logo-lockup">
        <span class="logo-mark"></span>
        <span class="logo-name">RTP Solutions</span>
      </div>
    </header>

    <h1 class="report-type">Inline Report</h1>

    <div class="hero-band" role="img" aria-label="Blue-toned photo of rooftop HVAC installation with pipework and fan units"></div>

    <h2 class="project-title">Testproject in Testplace</h2>
    <p class="project-meta">Measured by&nbsp; RTP Luchtregeling B.V. on 1-5-2017</p>
  </main>
</body>
</html>
```